Business card design needed

We need something on the back that allows the customer to get five stamps then the sixth visit they get 25 dollars to spend.
Business
Quality meat,value for money,spit roast hire, wholesale pubs clubs,cater for bbqs.kessel lane butchery 58 kessel lane.64390217.

```html
<!DOCTYPE html>
<html lang="en">
<head>
<meta charset="utf-8">
<title>Kessel Lane Butchery – Business Card</title>
<link rel="stylesheet" href="https://fonts.googleapis.com/css2?family=Saira+Extra+Condensed:wght@700&display=swap">
<style>
  :root {
    --card-edge-top: #2c3234;
    --card-edge-bottom: #7a8689;
    --panel-top: #151515;
    --panel-mid: #262829;
    --panel-bottom: #3d4547;
    --brand-red: #ea1a10;
    --steel-light: #e4e8ea;
    --steel-mid: #b9c0c3;
    --steel-dark: #8c9598;
  }
  html, body {
    margin: 0;
    padding: 0;
    width: 1200px;
    height: 741px;
    overflow: hidden;
    background: #ffffff;
  }
  .card {
    position: relative;
    width: 1200px;
    height: 741px;
    overflow: hidden;
    background: linear-gradient(180deg, var(--card-edge-top) 0%, var(--card-edge-bottom) 100%);
  }
  .card-art {
    position: absolute;
    inset: 0;
    width: 1200px;
    height: 741px;
    display: block;
  }
  .wordmark-text {
    font-family: "Saira Extra Condensed", "Arial Narrow", sans-serif;
    font-weight: 700;
    fill: var(--brand-red);
    text-transform: uppercase;
  }
</style>
</head>
<body>
  <main class="card">
    <svg class="card-art" viewBox="0 0 1200 741">
      <defs>
        <linearGradient id="panelShade" x1="0" y1="0" x2="0" y2="1">
          <stop offset="0" stop-color="var(--panel-top)"/>
          <stop offset="0.55" stop-color="var(--panel-mid)"/>
          <stop offset="1" stop-color="var(--panel-bottom)"/>
        </linearGradient>
        <linearGradient id="steelShade" x1="0" y1="0" x2="1" y2="1">
          <stop offset="0" stop-color="var(--steel-mid)"/>
          <stop offset="0.45" stop-color="var(--steel-light)"/>
          <stop offset="1" stop-color="var(--steel-dark)"/>
        </linearGradient>
      </defs>

      <path class="card-panel" role="img" aria-label="Dark metallic mesh background with faint crossed cleavers"
        fill="url(#panelShade)"
        d="M150 0 H1050 A150 150 0 0 0 1173 148 V563 A180 180 0 0 0 1021 723 H179 A180 180 0 0 0 27 563 V148 A150 150 0 0 0 150 0 Z"/>

      <rect class="cleaver-art" role="img" aria-label="Illustration of a steel meat cleaver"
        x="722" y="395" width="273" height="137" rx="8" fill="url(#steelShade)"/>

      <text class="wordmark-text" role="heading" aria-level="1">
        <tspan x="719" y="265" font-size="60" text-anchor="end" textLength="182" lengthAdjust="spacingAndGlyphs">Kessel</tspan>
        <tspan x="722" y="357" font-size="103" text-anchor="end" textLength="268" lengthAdjust="spacingAndGlyphs">Lane</tspan>
        <tspan x="716" y="459" font-size="113" text-anchor="end" textLength="433" lengthAdjust="spacingAndGlyphs">Butchery</tspan>
      </text>
    </svg>
  </main>
</body>
</html>
```